Redesign Home Page

We need a new home page with a white background. Our company provides singing instruction to students world wide, both in person and on line. We're looking for a very clean and open design with maximum white space. The main goal of the page will be to get users to sign up for our mailing list. The current site is www.kelvarsong.com. I think the new page can be a long page (scrolll down is ok), to allow for more white space while still using the text from the current page.
Updates

Project Deadline Extended
Reason: Hello to all Designers, I apologize for not giving feedback this weekend. We went out of town for the Memorial Day holiday and I had no internet. I will be extending the deadline to Thursday. -Marcus

Target Market(s)

Singers of all ages and abilities, especially beginners.

Industry/Entity Type

It Company

Requirements
Must have
• 1. A white background
2. Lots of open space
3. An email sign up form on the top right that reads:
a. “Improve Your Singing Now.
b. Sign up for our Free Video Series: Tone Quest
4. Testimonails: found on https://www.kelvarsong.com/tone-ascent
5. My logo with the piano
6. My photo
7. Learn about our Lessons in:
a. San Francisco
b. Alameda
8. On Line Programs:
a. Tone Ascent
b. Wavlo Lessons

Nice to have
• Link to current student page: http://kelvarsong.com/what-students-say/students2
Pictures of singers
Video box: Use Marcus_Example
Should not have
• See "KelvarSong Redesign" file for more details.

```html
<!DOCTYPE html>
<html lang="en">
<head>
<meta charset="utf-8">
<title>Marcus Halden School of Voice</title>
<link rel="stylesheet" href="https://fonts.googleapis.com/css2?family=Arimo:wght@400;700&display=swap">
<style>
:root{
  --blue:#27a2df;
  --blue-dark:#1686c0;
  --blue-pale:#e5f4fc;
  --ink:#2b2b2b;
  --text:#666;
  --muted:#999;
  --line:#d6d6d6;
  --white:#fff;
}
*{box-sizing:border-box;margin:0;padding:0}
html,body{width:1200px;height:2204px;overflow:hidden;background:var(--white)}
body{position:relative;font-family:"Arimo",Arial,sans-serif;color:var(--text)}
h1,h2,h3{font-weight:400}
.abs{position:absolute}
a{color:inherit;text-decoration:none}

/* header */
.brand{left:20px;top:24px;display:flex;align-items:center;gap:14px}
.brand-mark{width:70px;height:70px;border:5px solid var(--blue);border-radius:50%}
.brand-name{font-size:44px;font-weight:700;color:var(--blue);line-height:1}
.brand-tag{font-size:22px;color:var(--blue);margin-top:4px}
.account-btn{top:16px;height:40px;background:var(--blue);color:var(--white);font-size:20px;display:flex;align-items:center;justify-content:center;border-radius:4px 4px 0 0;box-shadow:0 3px 0 var(--blue-dark)}
.main-nav{left:399px;top:104px;display:flex;gap:7px}
.main-nav a{height:38px;padding:0 14px;border:1px solid var(--line);border-bottom:none;font-size:16px;color:var(--text);display:flex;align-items:center;border-radius:3px 3px 0 0}
.main-nav a.is-active{background:var(--blue);color:var(--white);border-color:var(--blue);padding:0 22px}
.nav-rule{left:0;top:141px;width:1200px;height:4px;background:var(--blue)}

/* hero */
.hero-photo{left:7px;top:167px;width:691px;height:428px;border:2px solid var(--blue);background:linear-gradient(90deg,#fafafa 0%,#d8d8d8 40%,#3a3a3a 70%,#9a9a9a 100%)}
.hero-title{left:24px;top:212px;font-size:38px;color:var(--blue);line-height:1.15}
.hero-sub{left:24px;top:306px;width:260px;font-size:26px;color:var(--ink);line-height:1.1}
.btn-outline{border:2px solid var(--blue);color:var(--blue);background:var(--white);font-size:17px;display:flex;align-items:center;justify-content:center;border-radius:0 0 4px 4px}
.thumbs{left:708px;top:210px;width:100px}
.thumb{width:100px;height:75px;background:linear-gradient(135deg,#5a4a3a,#b8a898);border:2px solid var(--white);margin-bottom:14px;outline:1px solid var(--line)}
.side-panel{left:852px;top:167px;width:341px;height:428px;background:var(--blue-pale);border:3px solid var(--blue);border-radius:4px}
.side-title{left:852px;top:198px;width:341px;text-align:center;font-size:25px;color:var(--blue-dark)}
.side-btn{left:877px;width:294px;height:74px;text-align:center;font-size:17px;line-height:1.3;display:flex;align-items:center;justify-content:center;border-radius:4px}
.side-btn.primary{background:var(--blue);color:var(--white);box-shadow:0 4px 0 var(--blue-dark)}
.side-btn.secondary{background:var(--white);color:var(--ink);border:2px solid var(--blue)}

/* sections */
.section-title{left:7px;font-size:28px;color:var(--blue)}
.body-copy{left:7px;width:1186px;font-size:14px;line-height:1.45;color:var(--text)}
.system-card{top:955px;width:213px;height:201px;background:var(--blue);border-radius:4px;display:flex;align-items:center;justify-content:center;color:var(--white);font-size:26px;font-weight:700;font-family:Georgia,serif}
.system-card.open{background:var(--white);border:2px solid var(--blue);color:var(--text);flex-direction:column;justify-content:flex-start;font-weight:400;font-family:"Arimo",sans-serif}
.system-card.open h3{font-size:22px;font-weight:400;color:var(--blue-dark);margin:22px 0 14px}
.system-card.open p{font-size:15px;line-height:1.4;padding:0 14px}
.btn-solid{background:var(--blue);color:var(--white);font-size:16px;display:flex;align-items:center;justify-content:center;border-radius:3px 3px 0 0;box-shadow:0 3px 0 var(--blue-dark)}

.col-title{top:1364px;font-size:20px;color:var(--blue-dark);text-align:center}
.col-box{top:1396px;height:282px;border:2px solid var(--blue);border-radius:4px}
.feature-list{left:30px;top:1418px;list-style:none}
.feature-list li{display:flex;gap:12px;font-size:19px;color:var(--ink);line-height:1.25;margin-bottom:18px}
.consult{left:416px;top:1534px;width:365px;text-align:center;font-size:18px;color:var(--ink);line-height:1.3}
.consult-link{left:416px;top:1620px;width:365px;text-align:center;font-size:18px;color:var(--blue)}
.form-label{left:852px;top:1410px;font-size:19px;color:var(--blue-dark)}
.field{left:852px;width:322px;height:44px;border:2px solid var(--blue);border-radius:4px;font-size:16px;color:#b5b5b5;padding:0 12px;display:flex;align-items:center}

/* feedback */
.fb-photo{top:1756px;width:210px;height:204px;border:3px solid var(--blue);background:linear-gradient(160deg,#6a5140,#c7a88a 50%,#3e2e24)}
.fb-name{top:1964px;font-size:19px;color:var(--blue-dark)}
.fb-country{top:1988px;font-size:13px;color:var(--muted)}
.fb-text{top:2006px;width:210px;font-size:14px;line-height:1.35;color:var(--text)}

/* footer */
.footer-rule{left:0;top:2096px;width:1200px;height:4px;background:var(--blue)}
.footer-nav{left:7px;top:2124px;width:1070px;display:flex;justify-content:space-between;font-size:18px;color:var(--ink);white-space:nowrap}
.footer-nav .sep{color:var(--muted)}
.footer-nav .is-active{color:var(--blue)}
.social{top:2118px;width:34px;height:34px;background:var(--blue);border-radius:3px}
.copyright{left:0;top:2168px;width:1200px;text-align:center;font-size:13px;color:var(--muted)}
.copyright a{color:var(--blue)}
</style>
</head>
<body>

<header>
  <div class="abs brand">
    <span class="brand-mark"></span>
    <div>
      <div class="brand-name">Marcus Halden</div>
      <div class="brand-tag">School of Voice</div>
    </div>
  </div>
  <a class="abs account-btn" style="left:906px;width:135px">Login</a>
  <a class="abs account-btn" style="left:1058px;width:130px">Sign up</a>
  <nav class="abs main-nav">
    <a class="is-active">Home</a>
    <a>Voice Lessons</a>
    <a>Blog</a>
    <a>What Student Say</a>
    <a>Meet the Instructors</a>
    <a>Tone Ascent</a>
  </nav>
  <div class="abs nav-rule"></div>
</header>

<section class="hero">
  <div class="abs hero-photo" role="img" aria-label="Portrait photograph of the voice teacher in a dark sweater"></div>
  <h1 class="abs hero-title">Tone<br>Ascent</h1>
  <p class="abs hero-sub">The most technically advanced Platform for singers</p>
  <a class="abs btn-outline" style="left:20px;top:539px;width:137px;height:40px">Learn more</a>

  <svg class="abs" style="left:744px;top:172px" width="28" height="26" viewBox="0 0 28 26"><path d="M14 0 28 16H20V26H8V16H0Z" fill="var(--blue)"/></svg>
  <div class="abs thumbs">
    <div class="thumb" role="img" aria-label="Teacher portrait thumbnail"></div>
    <div class="thumb" role="img" aria-label="Singers in a lesson thumbnail"></div>
    <div class="thumb" role="img" aria-label="Child at the piano thumbnail"></div>
    <div class="thumb" role="img" aria-label="Studio session thumbnail"></div>
  </div>
  <svg class="abs" style="left:744px;top:570px" width="28" height="26" viewBox="0 0 28 26"><path d="M14 26 28 10H20V0H8V10H0Z" fill="var(--blue)"/></svg>

  <aside>
    <div class="abs side-panel"></div>
    <h2 class="abs side-title">Marcus School of Voice</h2>
    <a class="abs side-btn primary" style="top:257px">In person Lessons<br>san Francisco or Alameda</a>
    <a class="abs side-btn secondary" style="top:362px">Online Training<br>Interactive Video</a>
    <a class="abs side-btn secondary" style="top:453px">Sign up for our<br>Free Singing Program</a>
  </aside>
</section>

<section class="welcome">
  <h2 class="abs section-title" style="top:624px">Wellcome to our Website</h2>
  <p class="abs body-copy" style="top:664px">Lorem Ipsum is simply dummy text of the printing and typesetting industry. Lorem Ipsum has been the industry's standard dummy text ever since the 1500s, when an unknown printer took a galley of type and scrambled it to make a type specimen book. It has survived not only five centuries, but also the leap into electronic typesetting, remaining essentially unchanged.</p>
  <p class="abs body-copy" style="top:758px">It was popularised in the 1960s with the release of Letraset sheets containing Lorem Ipsum passages, and more Lorem Ipsum is simply dummy text of the printing and typesetting industry. Lorem Ipsum has been the industry's standard dummy text ever since the 1500s, when an unknown printer took a galley of type and scrambled it to make a type specimen book. It has survived not only five centuries, but also the leap into electronic typesetting, remaining essentially unchanged. It was popularised in the 1960s with the release of Letraset sheets containing Lorem Ipsum passages, and more</p>
</section>

<section class="systems">
  <h2 class="abs section-title" style="top:876px">The Five Systems.</h2>
  <p class="abs" style="left:7px;top:914px;font-size:13px">Five essentials for a strong, <span style="color:var(--blue)">FREE voice</span></p>
  <div class="abs system-card" style="left:7px">Vocal cords</div>
  <div class="abs system-card open" style="left:250px">
    <h3>Air Control</h3>
    <p>Lorem Ipsum is simply dummy text of the printing and typesetting industry.</p>
  </div>
  <a class="abs btn-solid" style="left:285px;top:1121px;width:143px;height:32px;font-size:14px">Read more</a>
  <div class="abs system-card" style="left:492px">Outer Musicles</div>
  <div class="abs system-card" style="left:735px">Pharynx</div>
  <div class="abs system-card" style="left:977px">Larynx</div>
</section>

<section class="transformation">
  <h2 class="abs section-title" style="top:1186px">How Voice Transformation Works</h2>
  <p class="abs body-copy" style="top:1228px">After many years of work, I've decided that the effective transformation of the human voice is my life's work and passion. While on line methods of instruction are not as effective as in person lessons, I find that getting a foundational understanding of the voice that comes with Tone Ascent can greatly enhance your singing voice, whether you're currently studying with a teacher or working on your own.</p>
  <a class="abs btn-solid" style="left:1046px;top:1305px;width:147px;height:40px">Read more</a>
</section>

<section class="columns">
  <h3 class="abs col-title" style="left:7px;width:360px">Tone Ascent Available Now</h3>
  <div class="abs col-box" style="left:7px;width:360px"></div>
  <ul class="abs feature-list">
    <li><svg width="16" height="22" viewBox="0 0 16 22"><path d="M6 0h3v16a5 4 0 1 1-3-3.6Z M9 0c2 3 7 4 5 9 0-3-3-4-5-4Z" fill="var(--blue)"/></svg>Get Instant Access</li>
    <li><svg width="16" height="22" viewBox="0 0 16 22"><path d="M6 0h3v16a5 4 0 1 1-3-3.6Z M9 0c2 3 7 4 5 9 0-3-3-4-5-4Z" fill="var(--blue)"/></svg>Unique methods that are ideal<br>for voice health</li>
    <li><svg width="16" height="22" viewBox="0 0 16 22"><path d="M6 0h3v16a5 4 0 1 1-3-3.6Z M9 0c2 3 7 4 5 9 0-3-3-4-5-4Z" fill="var(--blue)"/></svg>The Most Advanced Platform<br>for On Line Singing Instruction</li>
    <li><svg width="16" height="22" viewBox="0 0 16 22"><path d="M6 0h3v16a5 4 0 1 1-3-3.6Z M9 0c2 3 7 4 5 9 0-3-3-4-5-4Z" fill="var(--blue)"/></svg>60+ Videos and Audio Workouts</li>
  </ul>
  <a class="abs btn-solid" style="left:103px;top:1632px;width:147px;height:44px;font-size:19px">Read More</a>

  <h3 class="abs col-title" style="left:416px;width:365px">Free Consultation with Marcus</h3>
  <div class="abs col-box" style="left:416px;width:365px"></div>
  <p class="abs consult">Marcus Halden has openings for a free<br>15 minute consultation over the phone.<br>If you have questions about your voice,</p>
  <a class="abs consult-link">click here to set up your time slot.</a>

  <h3 class="abs col-title" style="left:828px;width:365px">Connect with Us</h3>
  <div class="abs col-box" style="left:828px;width:365px"></div>
  <p class="abs form-label">Contact Form</p>
  <div class="abs field" style="top:1446px">Your Name</div>
  <div class="abs field" style="top:1502px">Phone</div>
  <div class="abs field" style="top:1560px">Email address</div>
  <a class="abs btn-solid" style="left:943px;top:1632px;width:147px;height:44px;font-size:19px">Submit</a>
</section>

<section class="feedback">
  <h2 class="abs section-title" style="top:1696px">Our Feedback</h2>
  <svg class="abs" style="left:40px;top:1838px" width="32" height="34" viewBox="0 0 32 34"><path d="M0 17 18 0V10H32V24H18V34Z" fill="var(--blue)"/></svg>
  <svg class="abs" style="left:1128px;top:1838px" width="32" height="34" viewBox="0 0 32 34"><path d="M32 17 14 0V10H0V24H14V34Z" fill="var(--blue)"/></svg>

  <div class="abs fb-photo" style="left:118px" role="img" aria-label="Student playing the piano"></div>
  <p class="abs fb-name" style="left:118px">Student,s name</p>
  <p class="abs fb-country" style="left:118px">Country name</p>
  <p class="abs fb-text" style="left:118px">Lorem Ipsum is simply dummy text of the printing Lorem Ipsum is simply dummy text of the printing</p>

  <div class="abs fb-photo" style="left:370px" role="img" aria-label="Student playing the piano"></div>
  <p class="abs fb-name" style="left:370px">Student,s name</p>
  <p class="abs fb-country" style="left:370px">Country name</p>
  <p class="abs fb-text" style="left:370px">Lorem Ipsum is simply dummy text of the printing Lorem Ipsum is simply dummy text of the printing</p>

  <div class="abs fb-photo" style="left:622px" role="img" aria-label="Student playing the piano"></div>
  <p class="abs fb-name" style="left:622px">Student,s name</p>
  <p class="abs fb-country" style="left:622px">Country name</p>
  <p class="abs fb-text" style="left:622px">Lorem Ipsum is simply dummy text of the printing Lorem Ipsum is simply dummy text of the printing</p>

  <div class="abs fb-photo" style="left:874px" role="img" aria-label="Student playing the piano"></div>
  <p class="abs fb-name" style="left:874px">Student,s name</p>
  <p class="abs fb-country" style="left:874px">Country name</p>
  <p class="abs fb-text" style="left:874px">Lorem Ipsum is simply dummy text of the printing Lorem Ipsum is simply dummy text of the printing</p>
</section>

<footer>
  <div class="abs footer-rule"></div>
  <nav class="abs footer-nav">
    <a class="is-active">Home</a><span class="sep">~</span>
    <a>About us</a><span class="sep">~</span>
    <a>Support</a><span class="sep">~</span>
    <a>KSMethod</a><span class="sep">~</span>
    <a>Privacy Policy</a><span class="sep">~</span>
    <a>Terms of us</a><span class="sep">~</span>
    <a>Sitemap</a><span class="sep">~</span>
    <a>Contact us</a>
  </nav>
  <span class="abs social" style="left:1120px"></span>
  <span class="abs social" style="left:1160px"></span>
  <p class="abs copyright">© Copyright 2014. <a>KelvarSong.com</a> . All Rights Reserved.</p>
</footer>

</body>
</html>
```